CSS design for a web application

We are currently building a web application in JAVA. The application uses a combination of a HTML template and CSS for the look and feel. We currenly have a very corporate look and feel for demo puposes, but we need to have some CSS designs that we can show to prospective customers. One of the functionalities of our application is the possibility to upload a customer's own (CSS) design in the application.

Our first customer is a high school in The Netherlands (12-18 year students) for children who are physically challenged. So the design should be easy to read, buttons should be easy to see, read and click and the different parts/texts on the website shouldn't be too close together. At the same time, we would like to avoid too much scrolling (especially horizontally). Go with a minimun screen resolution of 1024 x 768.

As our users are children, nice colours and other fun elements would be nice, while keeping a 'school like' appearance. Please use pictures and icons that our users will relate too. We want to communicate that our software is easy, fun and at the same time professional.

Our product is based on Tarvo Apps by Tarvo and thus Tarvo applications as Pluxo, Calendar, Tarvo Docs etc are all integrated in our software solution.

Find attached a static HTML file that contains our current CSS design. This should be used as a basis as it contains al the CSS elements that are used in the application. Please note that jQuery (javascript) knowledge is necessary.

Target Market(s)

Students at high school (age group 12/13 to 17/18). Users have physical disabilities that sometimes means they need special equipment/tools to operate their laptop.

Requirements
Must have
• Easy too navigate, buttons that are easy to see/use
Nice to have
• 'WOW' factor when people look at the design
Should not have
• buttons/text that is too small, too close together

```html
<!DOCTYPE html>
<html lang="en">
<head>
<meta charset="utf-8">
<title>Study Guide Engels – Lernova</title>
<link rel="stylesheet" href="https://fonts.googleapis.com/css2?family=Arimo:wght@400;700&family=Archivo+Narrow:wght@600;700&display=swap">
<style>
  :root {
    --bar-light: #fafafa;
    --bar-dark: #d9d9d9;
    --text: #111;
    --link-blue: #1a5aa0;
    --brand: #1f9fe0;
    --orange-light: #ffc46a;
    --orange: #f98a10;
    --orange-dark: #d96a00;
    --banner-light: #5ac6f0;
    --banner-dark: #1290cf;
    --nav-light: #7fd5f5;
    --nav-dark: #21a9df;
    --nav-border: #0f86c0;
    --panel: #a8def6;
    --row-a: #c3e6f5;
    --row-b: #c9cad9;
    --white: #fff;
    --german: #ffcf3f;
    --english: #ff6b6b;
    --french: #5b7cff;
    --economics: #3fd17a;
    --dutch: #ff8a1f;
    --chemistry: #b46cff;
  }
  * { box-sizing: border-box; margin: 0; padding: 0; }
  html, body { width: 1200px; height: 656px; overflow: hidden; }
  body { position: relative; background: var(--white); font-family: "Arimo", Arial, sans-serif; color: var(--text); }

  .top-bar { position: absolute; left: 0; top: 0; width: 1200px; height: 46px;
    background: linear-gradient(var(--bar-light), var(--bar-dark)); font-weight: 700; font-size: 15.5px; }
  .top-bar ul { position: absolute; top: 15px; list-style: none; display: flex; }
  .top-bar li + li::before { content: "|"; margin: 0 14px; }
  .apps { left: 19px; }
  .account { position: absolute; left: 657px; top: 14px; color: var(--link-blue); font-weight: 700; font-size: 15.5px; }
  .user-links { right: 19px; }

  .header { position: absolute; left: 0; top: 46px; width: 1200px; height: 62px;
    background: linear-gradient(#e9e9e9, #d4d4d4); }
  .brand { position: absolute; left: 36px; top: 16px; display: flex; align-items: center; gap: 8px;
    color: var(--brand); font-weight: 700; font-size: 27px; }
  .brand-dot { width: 24px; height: 24px; border-radius: 50%; background: var(--brand); }
  .search-field { position: absolute; left: 240px; top: 22px; width: 226px; height: 28px;
    background: var(--white); border: 1px solid #9a9a9a; }
  .search-button { position: absolute; left: 471px; top: 22px; width: 108px; height: 28px;
    background: linear-gradient(var(--orange-light), var(--orange)); border: 1px solid var(--orange-dark);
    color: var(--white); font-weight: 700; font-size: 15px; display: flex; align-items: center; justify-content: center; gap: 6px; }

  .banner { position: absolute; left: 0; top: 122px; width: 1200px; height: 58px;
    background: linear-gradient(90deg, var(--banner-dark), var(--banner-light) 70%, var(--banner-dark));
    border-top: 1px solid var(--nav-border); border-bottom: 1px solid var(--nav-border); }
  .menu-tab { position: absolute; left: 10px; top: 9px; width: 206px; height: 40px;
    background: linear-gradient(var(--orange-light), var(--orange)); border: 1px solid var(--orange-dark);
    color: var(--white); font-family: "Archivo Narrow", "Arial Narrow", sans-serif; font-weight: 700; font-size: 25px;
    padding: 4px 0 0 10px; }
  .page-title { position: absolute; left: 240px; top: 14px; color: var(--white);
    font-family: "Archivo Narrow", "Arial Narrow", sans-serif; font-weight: 700; font-size: 25px; }

  .side-nav { position: absolute; left: 0; top: 194px; width: 217px; height: 359px;
    background: var(--nav-border); padding: 8px 6px 0 15px; }
  .side-nav a { position: relative; display: block; height: 30px; margin-bottom: 2px; padding: 7px 0 0 20px;
    background: linear-gradient(var(--nav-light), var(--nav-dark)); color: var(--white);
    text-decoration: none; font-weight: 700; font-size: 14px; }
  .side-nav a.sub { padding-left: 63px; }
  .side-nav a.current { color: #0a2740; }
  .side-nav .nav-icon { position: absolute; right: 10px; top: 7px; }
  .subject-dot { position: absolute; left: 42px; top: 10px; width: 11px; height: 11px; border-radius: 50%; border: 1.5px solid var(--white); }

  .content { position: absolute; left: 236px; top: 194px; width: 964px; height: 378px; background: var(--panel); }
  .back-button { position: absolute; left: 12px; top: 10px; width: 107px; height: 30px;
    background: linear-gradient(var(--orange-light), var(--orange)); border: 1px solid var(--orange-dark);
    color: var(--white); font-size: 19px; display: flex; align-items: center; gap: 10px; padding-left: 8px; }
  .course-line { position: absolute; left: 179px; top: 14px; font-size: 16px; }
  .course-meta { position: absolute; left: 725px; top: 6px; font-size: 13.5px; line-height: 20px; }

  .table-body { position: absolute; left: 12px; top: 78px; width: 941px; height: 220px; background: var(--white); }
  .assignments { position: absolute; left: 12px; top: 52px; width: 941px; border-collapse: separate; border-spacing: 0 3px; }
  .assignments th { text-align: left; font-weight: 700; font-size: 14.5px; height: 24px; }
  .assignments td { height: 28px; font-size: 14px; }
  .assignments tbody tr:nth-child(odd) td { background: var(--row-a); }
  .assignments tbody tr:nth-child(even) td { background: var(--row-b); }
  .assignments a { color: var(--text); font-size: 16px; text-decoration: underline; margin-left: 7px; }
  .assignments .deadline { font-weight: 700; }

  .footer { position: absolute; left: 0; top: 600px; width: 1200px; height: 56px;
    background: linear-gradient(#f2f2f2, #d6d6d6); border-top: 1px solid #ccc;
    text-align: center; font-size: 13px; padding-top: 20px; }
</style>
</head>
<body>
  <nav class="top-bar">
    <ul class="apps"><li>Pluxo</li><li>Calender</li><li>Documents</li><li>Sites</li><li>Chat</li></ul>
    <span class="account">student@lms.lernova.nl</span>
    <ul class="user-links"><li>Settings</li><li>Help</li><li>Sign out</li></ul>
  </nav>

  <header class="header">
    <div class="brand"><span class="brand-dot"></span>lernova</div>
    <div class="search-field"></div>
    <div class="search-button">Search
      <svg width="18" height="18" viewBox="0 0 18 18"><circle cx="10" cy="7" r="5" fill="none" stroke="#fff" stroke-width="2"/><line x1="6.5" y1="10.5" x2="2" y2="15" stroke="#fff" stroke-width="2.5"/></svg>
    </div>
  </header>

  <div class="banner">
    <div class="menu-tab">Menu</div>
    <h1 class="page-title">Study Guide Engels</h1>
  </div>

  <aside class="side-nav">
    <a href="#">Home<svg class="nav-icon" width="16" height="16" viewBox="0 0 16 16"><path d="M2 8 8 2l6 6M4 7v7h8V7" fill="none" stroke="#fff" stroke-width="2"/></svg></a>
    <a href="#" class="current">Study Guide<svg class="nav-icon" width="16" height="16" viewBox="0 0 16 16"><path d="M3 2h10v12H3z M6 6h5M6 9h5" fill="none" stroke="#0a2740" stroke-width="1.8"/></svg></a>
    <a href="#" class="sub"><span class="subject-dot" style="background:var(--german)"></span>German</a>
    <a href="#" class="sub current"><span class="subject-dot" style="background:var(--english)"></span>English</a>
    <a href="#" class="sub"><span class="subject-dot" style="background:var(--french)"></span>French</a>
    <a href="#" class="sub"><span class="subject-dot" style="background:var(--economics)"></span>Economics</a>
    <a href="#" class="sub"><span class="subject-dot" style="background:var(--dutch)"></span>Dutch</a>
    <a href="#" class="sub"><span class="subject-dot" style="background:var(--chemistry)"></span>Chemistry</a>
    <a href="#">Books<svg class="nav-icon" width="16" height="16" viewBox="0 0 16 16"><path d="M2 3h5l1 1 1-1h5v10H9l-1 1-1-1H2z M8 4v10" fill="none" stroke="#fff" stroke-width="1.6"/></svg></a>
    <a href="#">Tests<svg class="nav-icon" width="16" height="16" viewBox="0 0 16 16"><path d="M2 8l4 4 8-9" fill="none" stroke="#fff" stroke-width="2.4"/></svg></a>
    <a href="#">Results<svg class="nav-icon" width="16" height="16" viewBox="0 0 16 16"><path d="M2 14h12" stroke="#fff" stroke-width="1.6"/><rect x="3" y="8" width="2.5" height="5" fill="#fff"/><rect x="7" y="4" width="2.5" height="9" fill="#fff"/><rect x="11" y="6" width="2.5" height="7" fill="#fff"/></svg></a>
  </aside>

  <main class="content">
    <div class="back-button">
      <svg width="20" height="12" viewBox="0 0 20 12"><path d="M8 1 3 6l5 5M16 1l-5 5 5 5" fill="none" stroke="#111" stroke-width="3"/></svg>Back
    </div>
    <p class="course-line">Engels door leraar@lms.lernova.nl voor m2@lms.lernova.nl</p>
    <p class="course-meta">English by Lernova<br>Eerste trimester (22-12-2010)</p>
    <div class="table-body"></div>
    <table class="assignments">
      <colgroup><col style="width:134px"><col style="width:598px"><col style="width:122px"><col></colgroup>
      <thead><tr><th>Assignment</th><th>Description</th><th>Deadline</th><th>Mark</th></tr></thead>
      <tbody>
        <tr><td><a href="#">Opdracht 1</a></td><td>Engels opdracht 1 door leraar@lms.lernova.nl voor m2@lms.lernova.nl</td><td class="deadline">22-12-2010</td><td></td></tr>
        <tr><td><a href="#">Opdracht 2</a></td><td>Engels opdracht 2 door leraar@lms.lernova.nl voor m2@lms.lernova.nl</td><td class="deadline">22-12-2010</td><td></td></tr>
        <tr><td><a href="#">Opdracht 3</a></td><td>Engels opdracht 3 door leraar@lms.lernova.nl voor m2@lms.lernova.nl</td><td class="deadline">22-12-2010</td><td></td></tr>
      </tbody>
    </table>
  </main>

  <footer class="footer">Copyright © 2010-2010 Lernova</footer>
</body>
</html>
```